Existing Website Requiring new Pages

I have an existing word press website that was built using elementor.
Website: www.tallowmerecare.com.au
I require the Vacancies page (https://www.tallowmerecare.com.au/vacancies/) to be modified to display our new properties along with minor tweaks to how the information is presented.
The vacancies to be displayed are the exactly the same as those that are located on the homepage of QDA website (https://qda.org.au/)
The new pages that link off the Vacancies tab will require custom design.
There are roughly 8 pages/properties to be incorporated. i wish for the design to be very similar to that displayed in the following link; https://www.zomplex.com.au/vacancies/merrylands
Along with this the back end has not been updated for the last 3 years so it also requires some maintenance.
Website is in the disability industry and the custom pages will display information relative to Property Vacancies.
I have attached a ZIP file with some design guides, the information for each of the properties (which will need to be modified to show our business name Tallowmere Healthcare) and the example of how it is to look based off the Zomplex website.
If you guys have any suggestions or ideas on how to make this more presentable or possible i'm open to your ideas.
People looking for SDA properties custom built for people with a disability
Disability
Coded - Design and coding required
5+ page

```html
<!DOCTYPE html>
<html lang="en">
<head>
<meta charset="utf-8">
<title>Vacancies – Tallowmere Healthcare</title>
<link rel="stylesheet" href="https://fonts.googleapis.com/css2?family=Roboto+Condensed:wght@700&family=Montserrat:wght@400;600&family=Nunito+Sans:wght@700&display=swap">
<style>
  :root{
    --ink:#111111;
    --text:#3a3a3a;
    --accent:#f28b6b;
    --link:#c56b5a;
    --teal:#14d3a8;
    --teal-soft:#dff6f0;
    --cream:#fbf1e2;
    --hero:#f7f7f7;
    --card:#ffffff;
    --page:#ffffff;
    --footer-dark:#1f1f1f;
    --magenta:#c2188a;
    --pink:#ee3d6b;
    --blue:#1e7fc0;
  }
  *{box-sizing:border-box;margin:0;padding:0}
  html,body{width:681px;height:1200px;overflow:hidden;background:var(--page)}
  body{position:relative;font-family:"Montserrat",sans-serif;color:var(--text)}

  .hero{position:absolute;left:0;top:0;width:681px;height:313px;overflow:hidden;
    background:linear-gradient(135deg,var(--cream) 0%,var(--hero) 30%,var(--hero) 62%,var(--teal-soft) 100%)}
  .brand{position:absolute;left:66px;top:20px;width:80px}
  .brand__dot{width:12px;height:12px;border-radius:50%;background:#e889c4;margin-bottom:3px}
  .brand__name{font-family:"Roboto Condensed",sans-serif;font-size:15px;color:#5a5a5a;line-height:1}
  .brand__sub{font-size:4.4px;letter-spacing:2.2px;color:var(--teal);margin-top:2px}
  .nav{position:absolute;top:32px;left:321px;display:flex;gap:13.5px;font-size:5.9px;font-weight:600;letter-spacing:.3px;color:#333}
  .nav__item--active{color:var(--accent)}
  .hero__title{position:absolute;left:92px;top:156px;font-family:"Roboto Condensed",sans-serif;font-size:35px;color:var(--ink);letter-spacing:.6px}
  .hero__photo{position:absolute;left:372px;top:64px;width:228px;height:228px;border-radius:50%;background:radial-gradient(circle at 60% 40%,#d8d3cc,#8b7260 70%,#4d3d30)}

  .card{position:absolute;width:176px;height:175px;background:var(--card);box-shadow:0 6px 22px rgba(0,0,0,.06)}
  .card__image{position:absolute;left:6px;top:6px;width:159px;height:101px}
  .card__title{position:absolute;left:10px;top:118px;font-family:"Roboto Condensed",sans-serif;font-size:14.5px;color:#222}
  .card__meta{position:absolute;left:11px;top:144px;font-family:"Nunito Sans",sans-serif;font-weight:700;font-size:7.8px;color:#444;display:flex;align-items:center;gap:3px}
  .img-suburb{background:linear-gradient(180deg,#c9d3de 0%,#b8b2a8 50%,#4f7a3a 100%)}
  .img-brick{background:linear-gradient(180deg,#6fa6d8 0%,#b4664a 50%,#5d8c34 100%)}
  .img-sky{background:linear-gradient(180deg,#3d93d9 0%,#e2d6ad 60%,#7ea25a 100%)}
  .img-cottage{background:linear-gradient(180deg,#8dbbe4 0%,#e3d3bf 55%,#5f8d3d 100%)}
  .img-palms{background:linear-gradient(180deg,#4aa4e6 0%,#d9cdb7 55%,#4f9a37 100%)}
  .img-orange{background:linear-gradient(180deg,#5aa9e6 0%,#c96a3a 55%,#6fb341 100%)}
  .img-dusk{background:linear-gradient(180deg,#f08a4b 0%,#4f4a55 50%,#7d8690 100%)}
  .img-villa{background:linear-gradient(180deg,#e9a26a 0%,#9da7a8 50%,#4c8f9e 100%)}
  .hover-bar{position:absolute;left:284px;top:538px;width:114px;height:8px;background:linear-gradient(90deg,var(--magenta),var(--pink))}

  .footer{position:absolute;left:0;top:989px;width:681px;height:172px;background:#fff;border-top:1px solid #f1f1f1}
  .footer__brand{position:absolute;left:65px;top:40px;width:120px}
  .footer__brand .brand__dot{width:20px;height:20px}
  .footer__brand .brand__name{font-size:22px}
  .footer__brand .brand__sub{font-size:6.4px;letter-spacing:3.5px}
  .contact{position:absolute;left:62px;top:119px;font-size:7.3px;color:var(--link);line-height:13.3px}
  .contact li{list-style:none;display:flex;align-items:center;gap:5px}
  .social{position:absolute;left:308px;top:31px;display:flex;flex-direction:column;gap:4.3px}
  .social span{width:20px;height:20px;border-radius:50%}
  .col{position:absolute;top:25px;width:136px}
  .col--accom{left:364px}
  .col--services{left:515px}
  .col__head{font-size:8.3px;font-weight:400;color:#222;letter-spacing:.3px;border-left:1.5px solid var(--blue);padding-left:8px;height:9px;line-height:9px;margin-bottom:10px}
  .col li{list-style:none;font-size:7.3px;color:var(--link);line-height:13px;padding:4px 0;border-top:1px solid #e6e6e6}
  .col li:last-child{border-bottom:1px solid #e6e6e6}
  .copyright{position:absolute;left:0;top:1161px;width:681px;height:39px;background:var(--footer-dark);color:#d0d0d0;font-size:5.6px;text-align:center;line-height:39px}
</style>
</head>
<body>

<header class="hero">
  <div class="brand">
    <div class="brand__dot"></div>
    <div class="brand__name">Tallowmere</div>
    <div class="brand__sub">HEALTHCARE</div>
  </div>
  <nav class="nav">
    <span>HOME</span><span>ABOUT US</span><span class="nav__item--active">WHAT WE DO ˅</span><span>REFERRALS</span><span>FEEDBACK</span><span>CONTACT US</span>
  </nav>
  <h1 class="hero__title">VACANCIES</h1>
  <div class="hero__photo" role="img" aria-label="Photo of a woman in a wheelchair working on a laptop by a window"></div>
</header>

<main>
  <article class="card" style="left:63px;top:363px"><div class="card__image img-suburb" role="img" aria-label="Photo of the Penrith home"></div><h2 class="card__title">Penrith</h2><p class="card__meta"><svg width="11" height="6" viewBox="0 0 11 6"><path d="M0 0v6M0 4h11v2M3 2h8v2" stroke="#555" stroke-width="1.4" fill="none"/></svg>4 Bedroom SIL Home</p></article>
  <article class="card" style="left:252px;top:363px"><div class="card__image img-brick" role="img" aria-label="Photo of the Mount Druitt brick home"></div><h2 class="card__title">Mount Druitt</h2><p class="card__meta"><svg width="11" height="6" viewBox="0 0 11 6"><path d="M0 0v6M0 4h11v2M3 2h8v2" stroke="#555" stroke-width="1.4" fill="none"/></svg>4 Bedroom SIL Home</p></article>
  <article class="card" style="left:442px;top:363px"><div class="card__image img-sky" role="img" aria-label="Photo of the Casula home"></div><h2 class="card__title">Casula</h2><p class="card__meta"><svg width="11" height="6" viewBox="0 0 11 6"><path d="M0 0v6M0 4h11v2M3 2h8v2" stroke="#555" stroke-width="1.4" fill="none"/></svg>4 Bedroom SIL Home</p></article>
  <div class="hover-bar"></div>

  <article class="card" style="left:63px;top:563px"><div class="card__image img-cottage" role="img" aria-label="Photo of the Eastwood cottage"></div><h2 class="card__title">Eastwood</h2><p class="card__meta"><svg width="11" height="6" viewBox="0 0 11 6"><path d="M0 0v6M0 4h11v2M3 2h8v2" stroke="#555" stroke-width="1.4" fill="none"/></svg>4 Bedroom SIL Home</p></article>
  <article class="card" style="left:252px;top:563px"><div class="card__image img-palms" role="img" aria-label="Photo of the Baulkham Hills home"></div><h2 class="card__title">Baulkham Hills</h2><p class="card__meta"><svg width="11" height="6" viewBox="0 0 11 6"><path d="M0 0v6M0 4h11v2M3 2h8v2" stroke="#555" stroke-width="1.4" fill="none"/></svg>4 Bedroom SIL Home</p></article>
  <article class="card" style="left:442px;top:563px"><div class="card__image img-orange" role="img" aria-label="Photo of the Merrylands home"></div><h2 class="card__title">Merrylands</h2><p class="card__meta"><svg width="11" height="6" viewBox="0 0 11 6"><path d="M0 0v6M0 4h11v2M3 2h8v2" stroke="#555" stroke-width="1.4" fill="none"/></svg>4 Bedroom SIL Home</p></article>

  <article class="card" style="left:158px;top:760px"><div class="card__image img-dusk" role="img" aria-label="Photo of a modern Mount Druitt home at dusk"></div><h2 class="card__title">Mount Druitt</h2><p class="card__meta"><svg width="11" height="6" viewBox="0 0 11 6"><path d="M0 0v6M0 4h11v2M3 2h8v2" stroke="#555" stroke-width="1.4" fill="none"/></svg>4 Bedroom SIL Home</p></article>
  <article class="card" style="left:347px;top:760px"><div class="card__image img-villa" role="img" aria-label="Photo of the Rooty Hill home with a pool at sunset"></div><h2 class="card__title">Rooty Hill</h2><p class="card__meta"><svg width="11" height="6" viewBox="0 0 11 6"><path d="M0 0v6M0 4h11v2M3 2h8v2" stroke="#555" stroke-width="1.4" fill="none"/></svg>4 Bedroom SIL Home</p></article>
</main>

<footer class="footer">
  <div class="brand footer__brand">
    <div class="brand__dot"></div>
    <div class="brand__name">Tallowmere</div>
    <div class="brand__sub">HEALTHCARE</div>
  </div>
  <ul class="contact">
    <li><svg width="8" height="6" viewBox="0 0 8 6"><rect x=".5" y=".5" width="7" height="5" fill="none" stroke="var(--pink)"/><path d="M.5 .5l3.5 3 3.5-3" fill="none" stroke="var(--pink)"/></svg>Email: info@tallowmerecare.com.au</li>
    <li><svg width="8" height="8" viewBox="0 0 8 8"><path d="M1 1l2 0 1 2-1 1c.5 1 1 1.5 2 2l1-1 2 1v2C4 8 0 4 1 1z" fill="var(--pink)"/></svg>Phone: +61 0400 318 264</li>
    <li><svg width="8" height="8" viewBox="0 0 8 8"><circle cx="4" cy="4" r="3.4" fill="none" stroke="var(--pink)"/><path d="M4 2v2l1.5 1" stroke="var(--pink)" fill="none"/></svg>Operating Hours: 9AM To 5PM Monday - Friday</li>
  </ul>
  <div class="social" aria-label="Partner badge and social links">
    <span style="background:#5b2a86"></span>
    <span style="background:#1d5fa8"></span>
    <span style="background:#222"></span>
    <span style="background:#1e7fc0"></span>
  </div>
  <div class="col col--accom">
    <h3 class="col__head">ACCOMMODATION</h3>
    <ul>
      <li>Supported Independent Living (SIL)</li>
      <li>Specialist Disability<br>Accommodation (SDA)</li>
      <li>Short term Accommodation<br>(Respite)</li>
      <li>Vacancies</li>
    </ul>
  </div>
  <div class="col col--services">
    <h3 class="col__head">WHAT WE DO</h3>
    <ul>
      <li>In Home Care</li>
      <li>Social &amp; Community Services</li>
      <li>Therapeutic Supports</li>
      <li>Support Coordination</li>
      <li>Home Modifications</li>
    </ul>
  </div>
</footer>
<div class="copyright">© Copyright 2024| Tallowmere Healthcare | All Rights Reserved.</div>

</body>
</html>
```